BrightLoop (1 page) homepage re-design

Our homepage needs a face-lift! We need our homepage on our website re-designed with a fresh and current look and feel. We have all the details, colour codes and a rough wireframe ready, but need a talented designer to put some personality into our ideas.

What we do: BrightLoop is a digital marketing agency with offices in Australia (Sydney) and South Africa (Cape Town). We specialise in SEO, PPC (otherwise known as Zentro PayLine or SEM), content marketing and Zentro Tallyboard. We use these tools to help our clients realise their business dreams.

VISUAL

Style / theme of the design:
Clean, simplistic, fun, flow.

Websites we draw inspiration from:
This is the theme we want to use to build the website
http://demo.vormalayouts.example/vl/?theme=Pebbled
Inspiration:
https://www.ondrapromo.example/
https://www.nelvagrowth.example.au/
https://quimbel.example.au/
https://torvin.layout-works.example/forum/

What we like about the site:
Clean, simple design, good use of white space. The subtle changing background colours, strong contrast with text. Not too busy or distracting.

What we don’t want: Too many different colours.

Target Market(s)

Our target audience: Marketing Managers of small to medium size businesses in Australia.

Industry/Entity Type

Marketing

Number of Pages Required

1 page

Font styles to use
Sans Serif

Requirements
Must have
• Elements to be added on homepage in order and as seen in attachments:
• - Section 1: Video with team as image and a play button add the heading: We help smart marketing managers achieve their KPIs [line break] and reduce their digital marketing overwhelm.
• - Section 2: Solutions section with the 6 solutions displayed in a row.
• - Section 3: Register Free Webinar with video
• - Section 4: Please add 3 case studies (as seen in attached docs there is only 1 but please add 3 below each other)
• - Section 5: Clients. Please add all client logo’s (black and white)
• - Section 6: Our Blog (as seen attached)
• - Section 7: Conferences Attended (please add the title and a paragraph of lorem Ipsom below) and then please add all conference logo’s attached below.
• - Section 8: In The Media (please add all logo’s titled media) white background
• - Section 9: Footer (dark grey footer) add our Zentro honoured affiliate logo here please
• - Section10: Footer - include:
• - Social logos (WorkMesh, Blipster, Pallwall, ReelDrop, Zentro Hub)
• - Navigation
• - Contact details (name, address, phone number, email)
• Colour codes:
• We want to use light greys, white and charcoal grey for the backgrounds with a pop of our green colour to bring out our branding and all CTA’s to be orange, colour codes below:
• Light grey: #F2F2F2
• Charcoal grey: #161616
• Green: #428E29
• CTA’s: #de7532
• PLEASE NOTE: Please see attached pdf titled: homepagecopybrief.pdf for all the titles and statistics that need to go on the homepage
Should not have
• Too much colour, icons should not be different colours

```html
<!DOCTYPE html>
<html lang="en">
<head>
<meta charset="utf-8">
<title>BrightLoop — Home</title>
<link rel="stylesheet" href="https://fonts.googleapis.com/css2?family=Lato:wght@300;400;700&display=swap">
<style>
  :root{
    --green:#0a960a;
    --green-soft:#c9f3c9;
    --green-pale:#e9fbe9;
    --text:#1d1d1d;
    --body:#333333;
    --light-grey:#f2f2f2;
    --white:#ffffff;
    --cta:#f7941d;
  }
  *{box-sizing:border-box;margin:0;padding:0}
  html,body{width:1200px;height:1200px;overflow:hidden;background:var(--white)}
  body{position:relative;font-family:"Lato",sans-serif;color:var(--text)}

  .card{position:absolute;background:var(--white);border:3px solid var(--green-soft);box-shadow:0 0 6px var(--green-soft);text-align:center}
  .card p{font-size:13.6px;line-height:25.6px;font-weight:400;color:var(--body)}
  .card--active{background:var(--green);border-color:var(--green);box-shadow:none}
  .card--active p{color:var(--white)}
  .card--top{top:-30px;height:80px;width:298px;padding-top:28px}
  .card--solution{top:178px;height:271px;width:298px}
  .card h3{font-weight:400;font-size:19px;line-height:26px;margin:0 auto 14px;color:var(--text)}
  .solution__icon{position:absolute;top:98px;width:144px;height:144px;border-radius:50%;background:var(--white);border:2px solid var(--green-pale);box-shadow:0 0 0 6px rgba(201,243,201,.35)}
  .solution__icon span{position:absolute;inset:6px;border-radius:50%;border:3px solid var(--green-soft);background:radial-gradient(circle,#dff6df 0 38%,var(--white) 40%)}

  .webinar{position:absolute;top:524px;left:0;width:1200px;height:380px;background:var(--light-grey)}
  .webinar__video{position:absolute;left:130px;top:77px;width:457px;height:227px;background:var(--white);padding:7px 8px}
  .webinar__photo{width:100%;height:100%;background:linear-gradient(120deg,#a9d79a 0%,#6fae5a 45%,#2f5e22 100%)}
  .webinar__play{position:absolute;left:199px;top:92px;width:61px;height:43px}
  .webinar__form{position:absolute;left:670px;top:78px;width:390px;text-align:center}
  .webinar h2{font-weight:400;font-size:24px;color:var(--green);margin-bottom:8px}
  .webinar__meta{font-size:13.6px;line-height:25.6px;font-weight:400;color:var(--body)}
  .webinar__input{margin:16px 0 0 7px;width:367px;height:54px;border:2px solid var(--green);border-radius:8px;background:var(--white);font:400 14px "Lato",sans-serif;color:var(--body);text-align:left;padding:16px 12px}
  .cta{position:absolute;left:77px;top:196px;width:211px;height:41px;border-radius:21px;background:var(--cta);color:var(--white);font-size:17px;display:flex;align-items:center;justify-content:center;gap:38px;padding-left:30px}

  .media{position:absolute;top:950px;left:0;width:1200px;text-align:center}
  .media h2{font-weight:400;font-size:30px;color:var(--green)}
  .media__rule{width:72px;height:2px;background:var(--green-soft);margin:10px auto 14px}
  .media__intro{font-size:13.6px;font-weight:400;color:var(--body)}
  .media__logo{position:absolute;top:148px;width:222px;height:120px;border:4px solid var(--green-soft);background:var(--white);display:flex;align-items:flex-start;justify-content:center;padding-top:44px;font-weight:700;font-size:22px;color:#111;line-height:24px;overflow:hidden}
  .media__arrow{position:absolute;top:198px;width:26px;height:26px}
</style>
</head>
<body>

  <section class="solutions">
    <div class="card card--top" style="left:116px"><p>using 'Content here</p></div>
    <div class="card card--top card--active" style="left:449px"><p>using 'Content here</p></div>
    <div class="card card--top" style="left:778px"><p>using 'Content here</p></div>

    <article class="card card--solution" style="left:116px">
      <div style="height:91px"></div>
      <h3>DATA/KPA's</h3>
      <p>It is a long established fact that a reader will<br>be distracted by the readable content of a<br>page when looking at its layout. The point of<br>using 'Content here</p>
    </article>
    <article class="card card--solution" style="left:446px">
      <div style="height:91px"></div>
      <h3>INCREASE ENGAGMENT</h3>
      <p>It is a long established fact that a reader will<br>be distracted by the readable content of a<br>page when looking at its layout. The point of<br>using 'Content here</p>
    </article>
    <article class="card card--solution" style="left:776px">
      <div style="height:83px"></div>
      <h3 style="margin-bottom:12px">MARKETING STRATEGY<br>/BUDGETING</h3>
      <p>It is a long established fact that a reader will<br>be distracted by the readable content of a<br>page when looking at its layout. The point of<br>using 'Content here</p>
    </article>

    <div class="solution__icon" style="left:194px" role="img" aria-label="Data chip icon"><span></span></div>
    <div class="solution__icon" style="left:526px" role="img" aria-label="Engagement network icon"><span></span></div>
    <div class="solution__icon" style="left:852px" role="img" aria-label="Budget document and calculator icon"><span></span></div>
  </section>

  <section class="webinar">
    <div class="webinar__video">
      <div class="webinar__photo" role="img" aria-label="Video still of a man working at a laptop"></div>
      <svg class="webinar__play" viewBox="0 0 61 43" aria-hidden="true">
        <rect x="1.5" y="1.5" width="58" height="40" rx="9" fill="#1d8f1d" stroke="#fff" stroke-width="3"/>
        <path d="M22 10 L41 21.5 L22 33 Z" fill="none" stroke="#fff" stroke-width="3" stroke-linejoin="round"/>
      </svg>
    </div>
    <div class="webinar__form">
      <h2>SIGNUP FOR OUR FREE WEBINAR</h2>
      <p class="webinar__meta">TITLE: ZENTRO TALLYBOARD MASTERY<br>WEDNESDAY, FEBRUARY 7 AT 2 P.M. ET / 11 A.M. PT</p>
      <div class="webinar__input">Your Email Address</div>
      <div class="cta">SIGNUP
        <svg width="22" height="22" viewBox="0 0 22 22" aria-hidden="true"><circle cx="11" cy="11" r="11" fill="#fff"/><path d="M9 6 L14 11 L9 16" fill="none" stroke="#f7941d" stroke-width="3"/></svg>
      </div>
    </div>
  </section>

  <section class="media">
    <h2>IN THE MEDIA</h2>
    <div class="media__rule"></div>
    <p class="media__intro">It is a long established fact that a reader will be distracted by the readable content of a page when looking at its layout. The</p>

    <svg class="media__arrow" style="left:71px" viewBox="0 0 26 26" aria-label="Previous"><circle cx="13" cy="13" r="13" fill="#f7941d"/><path d="M15 7 L9 13 L15 19" fill="none" stroke="#fff" stroke-width="3.5"/></svg>
    <div class="media__logo" style="left:130px">Tastewell</div>
    <div class="media__logo" style="left:369px;padding-top:22px;font-size:20px">The Harbour<br>Morning Gazette</div>
    <div class="media__logo" style="left:607px">shopfront</div>
    <div class="media__logo" style="left:846px;font-size:19px">The Evening Courier</div>
    <svg class="media__arrow" style="left:1093px" viewBox="0 0 26 26" aria-label="Next"><circle cx="13" cy="13" r="13" fill="#f7941d"/><path d="M11 7 L17 13 L11 19" fill="none" stroke="#fff" stroke-width="3.5"/></svg>
  </section>

</body>
</html>
```